Free Charity Events from KOVAPLAY

The purpose of the landing page is to get all visitors excited about playing in our Free $500 Charity Tournaments. The visitors who click on the landing page will receive 3 free entries into 3 different $500 Charity Tournaments. A $500 Blackjack Tournament, a $500 Texas Holdem Tournament, and a $500 Baccarat Tournament.

We also offer Free Qualifying games 24/7, where players can earn additional entries into our real paying tournaments.

We will reward the winners in each tournament with a share of the $500 and we will reward a worthy cause or charity with $500 as well.

The money comes from advertising shown during the qualifying game.

Our website is currently being developed on our teams development server. Here is a private link to the site. https://dev.kovaplay.net Attached are vector images of our logo.

Also attached are two attempts we made at a landing page.

Target Market(s)

Social Game Players

Industry/Entity Type

Games

Contact Information for Business Card

The purpose of the business card will be to promote our Free Charity Games. There will be a code hand written on the card. (Meaning we will need a white box to write the code in) If the holder of the card enters that code during registration, they will receive 3 free entries into our real cash tournaments. The giver of the card will receive the affiliate bonus for referring a new player.

Font styles to use
Serif
Sans Serif

Colors
9bcb3c
0292cd
ec1f27

Requirements
Must have
• Excitement, i also like humor but that isn't a must, excitement is.
Nice to have
• Humor
Should not have
• Too many words, we are looking for that image that says at least a few hundred words.

```html
<!DOCTYPE html>
<html lang="en">
<head>
<meta charset="utf-8">
<title>KOVAPLAY – Free Charity Tournaments</title>
<link rel="stylesheet" href="https://fonts.googleapis.com/css2?family=Noto+Sans:ital,wght@0,400;0,700;0,800;1,800&display=swap">
<style>
  :root {
    --blue: #3673ad;
    --green: #8bad48;
    --green-soft: #a7c577;
    --red: #d0021b;
    --paper: #ffffff;
    --photo-light: #f3efed;
    --photo-mid: #d9cfc9;
    --photo-warm: #c9b3a4;
    --social-1: #3b5998;
    --social-2: #4e7da6;
    --social-3: #cf2e2e;
    --social-4: #4f8fd6;
  }
  * { margin: 0; padding: 0; box-sizing: border-box; }
  html, body { width: 1200px; height: 878px; overflow: hidden; background: var(--paper); }
  body { font-family: "Noto Sans", Verdana, sans-serif; }
  .landing { position: relative; width: 1200px; height: 878px; overflow: hidden; background: var(--paper); }
  .hero-photo {
    position: absolute; left: 520px; top: 0; width: 680px; height: 878px;
    background:
      radial-gradient(ellipse 260px 360px at 430px 330px, var(--photo-warm) 0%, rgba(201,179,164,0) 100%),
      radial-gradient(ellipse 360px 420px at 520px 640px, var(--photo-mid) 0%, rgba(217,207,201,0) 100%),
      linear-gradient(90deg, var(--paper) 0%, var(--photo-light) 35%, var(--photo-light) 100%);
  }
  .brand { position: absolute; left: 24px; top: 56px; display: flex; align-items: center; gap: 18px; }
  .brand-dot { width: 118px; height: 118px; border-radius: 50%; background: var(--blue); }
  .brand-name { font-weight: 800; font-size: 82px; color: var(--blue); letter-spacing: 1px; line-height: 1; }
  .tagline { position: absolute; left: 27px; top: 188px; font-weight: 700; font-size: 41px; color: var(--red); letter-spacing: 0.5px; }
  .headline { position: absolute; left: 37px; top: 264px; }
  .headline-main { font-weight: 800; font-size: 62px; color: var(--blue); line-height: 1.05; letter-spacing: 1px; }
  .headline-sub { font-weight: 800; font-style: italic; font-size: 35px; line-height: 1.22; letter-spacing: 0.5px; }
  .headline-sub .green { color: var(--green); }
  .headline-sub .red { color: var(--red); }
  .headline-sub .blue { color: var(--blue); }
  .games { position: absolute; left: 36px; top: 422px; display: flex; gap: 16px; font-size: 27px; color: var(--green); list-style: none; }
  .games li { display: flex; align-items: center; gap: 4px; }
  .games svg { width: 20px; height: 20px; }
  .signup { position: absolute; left: 0; top: 508px; width: 550px; text-align: center; }
  .signup-lead { font-weight: 700; font-size: 23px; color: var(--blue); line-height: 1.2; letter-spacing: 0.3px; }
  .email-field {
    display: block; margin: 17px 0 0 67px; width: 394px; height: 36px;
    border: 1px solid #a9bfd6; border-radius: 18px; background: rgba(255,255,255,0.6);
    font-family: inherit; font-weight: 700; font-size: 23px; color: var(--green); text-align: center; line-height: 34px;
  }
  .cta {
    display: block; margin: 20px 0 0 157px; width: 216px; height: 36px; background: var(--green-soft);
    color: var(--paper); font-weight: 700; font-size: 18px; letter-spacing: 1px; line-height: 36px; text-align: center;
  }
  .share { position: absolute; left: 0; top: 702px; width: 520px; text-align: center; }
  .share-title { font-weight: 700; font-size: 18px; color: var(--blue); letter-spacing: 0.5px; }
  .share-links { display: flex; gap: 6px; justify-content: center; margin-top: 17px; padding-right: 0; list-style: none; }
  .share-links li { width: 44px; height: 44px; border-radius: 50%; }
  .share-links .s1 { background: var(--social-1); }
  .share-links .s2 { background: var(--social-2); }
  .share-links .s3 { background: var(--social-3); }
  .share-links .s4 { background: var(--social-4); }
  .legal { position: absolute; left: 0; top: 843px; width: 520px; text-align: center; font-size: 8.5px; color: var(--blue); letter-spacing: 0.3px; }
</style>
</head>
<body>
<main class="landing">
  <div class="hero-photo" role="img" aria-label="Photo of a delighted young woman cheering with a raised fist while looking at her phone, faded softly into white"></div>

  <div class="brand">
    <span class="brand-dot"></span>
    <span class="brand-name">KOVAPLAY</span>
  </div>
  <p class="tagline">Where Everyone Wins!</p>

  <h1 class="headline">
    <span class="headline-main">PLAY FREE</span><br>
    <span class="headline-sub"><span class="green">IN OUR THREE </span><span class="red">$500</span><br><span class="blue">CHARITY TOURNAMENTS</span></span>
  </h1>

  <ul class="games">
    <li><svg viewBox="0 0 24 24"><path d="M12 2l2.9 6.6 7.1.6-5.4 4.7 1.6 7-6.2-3.7-6.2 3.7 1.6-7L2 9.2l7.1-.6z" fill="none" stroke="#d0021b" stroke-width="2"/></svg>Blackjack</li>
    <li><svg viewBox="0 0 24 24"><path d="M12 2l2.9 6.6 7.1.6-5.4 4.7 1.6 7-6.2-3.7-6.2 3.7 1.6-7L2 9.2l7.1-.6z" fill="none" stroke="#d0021b" stroke-width="2"/></svg>Holdem</li>
    <li><svg viewBox="0 0 24 24"><path d="M12 2l2.9 6.6 7.1.6-5.4 4.7 1.6 7-6.2-3.7-6.2 3.7 1.6-7L2 9.2l7.1-.6z" fill="none" stroke="#d0021b" stroke-width="2"/></svg>Baccarat</li>
  </ul>

  <section class="signup">
    <p class="signup-lead">Subscribe email and get 3 free entries<br>into 3 different $500 Charity Tournaments</p>
    <span class="email-field">Enter Your Email id here</span>
    <span class="cta">GET FREE ENTRIES</span>
  </section>

  <section class="share">
    <p class="share-title">SHARE WITH US</p>
    <ul class="share-links">
      <li class="s1"></li><li class="s2"></li><li class="s3"></li><li class="s4"></li>
    </ul>
  </section>

  <p class="legal">© KOVAPLAY, ALL RIGHTS RESERVED 2019</p>
</main>
</body>
</html>
```